Theatre Company needs poster for a Christmas show.

We need a poster for an annual Christmas musical show call "A Plum Hush". The style is Jazzy/Lounge Christmas songs. The poster should be a mid-centry modern, Gilt Row-style design. I have attached the past year's poster for reference. The poster should include "VelNOVA Professional Series presents A Plum Hush" the date "December 18th, 2015" our phone number "512-555-0148 ext 207" and our website "vel-nova.org". The poster should also include the logos of our title sponsors (attached).

Target Market(s)

Lakeway, Texas residents, Adults, 21+

Industry/Entity Type

It Company

Font styles to use
Sans Serif

Requirements
Must have
• VelNOVA logo
• Show title "A Plum Hush"
• Date: December 18th, 2015
• Phone number: 512-555-0148 ext 207
• Web site: vel-nova.org
• Sponsor logos at the bottom (attached)
• Mid-century modern, Gilt Row-style design
• Christmas/Winter colors
Nice to have
• Singer/piano/microphone imagery
• cocktail imagery

```html
<!DOCTYPE html>
<html lang="en">
<head>
<meta charset="utf-8">
<title>A Plum Hush — VelNOVA Professional Series</title>
<link rel="stylesheet" href="https://fonts.googleapis.com/css2?family=Quicksand:wght@700&family=Libre+Baskerville&family=Montserrat:wght@500;700&display=swap">
<style>
  :root {
    --night: #231f20;
    --snow: #ffffff;
    --cream: #efe3c8;
    --teal: #5e9ea0;
    --berry: #c8323a;
    --ink: #3a3a3a;
    --muted: #7a7a7a;
  }
  * { margin: 0; padding: 0; box-sizing: border-box; }
  html, body { width: 800px; height: 1200px; overflow: hidden; background: var(--night); }
  .poster {
    position: relative;
    width: 800px;
    height: 1200px;
    background: var(--night);
    overflow: hidden;
    font-family: "Montserrat", sans-serif;
  }
  .brand-tab {
    position: absolute;
    top: 0; right: 0;
    width: 150px; height: 54px;
    background: var(--snow);
    border-bottom-left-radius: 28px;
    display: flex; align-items: center; justify-content: center;
    font: 700 22px "Montserrat", sans-serif;
    color: var(--berry);
    letter-spacing: 0.5px;
  }
  .tree-art {
    position: absolute;
    left: 110px; top: 70px;
    width: 580px; height: 690px;
  }
  .show-title {
    position: absolute;
    left: 100px; top: 765px;
    width: 460px; height: 190px;
    color: var(--snow);
    font-family: "Quicksand", sans-serif;
    font-weight: 700;
    text-transform: lowercase;
  }
  .title-article {
    position: absolute;
    left: 0; top: 0;
    font-size: 240px;
    line-height: 190px;
  }
  .title-word {
    position: absolute;
    left: 150px;
    font-size: 112px;
    line-height: 92px;
    letter-spacing: -2px;
  }
  .title-word.first { top: 0; }
  .title-word.second { top: 92px; }
  .show-date {
    position: absolute;
    left: 455px; top: 952px;
    font: 28px "Libre Baskerville", serif;
    line-height: 36px;
    color: var(--snow);
    white-space: nowrap;
  }
  .sponsor-band {
    position: absolute;
    left: 0; bottom: 0;
    width: 800px; height: 180px;
  }
  .sponsor-band svg { position: absolute; left: 0; top: 0; }
  .sponsor-heading {
    position: absolute;
    top: 40px; width: 100%;
    text-align: center;
    font: 700 22px "Montserrat", sans-serif;
    color: var(--ink);
    letter-spacing: 1px;
  }
  .sponsor-list {
    position: absolute;
    top: 80px; left: 170px; right: 170px;
    display: flex; justify-content: space-between; align-items: center;
  }
  .sponsor-name {
    font: 700 17px "Montserrat", sans-serif;
    color: var(--ink);
    display: flex; align-items: center; gap: 6px;
    white-space: nowrap;
  }
  .sponsor-name .dot { width: 10px; height: 10px; border-radius: 50%; background: var(--teal); }
  .ticket-line {
    position: absolute;
    bottom: 16px; left: 160px; right: 160px;
    display: flex; justify-content: space-between;
    font: 500 15px "Montserrat", sans-serif;
    color: var(--muted);
    white-space: nowrap;
  }
</style>
</head>
<body>
<main class="poster">
  <div class="brand-tab">VelNOVA</div>

  <svg class="tree-art" viewBox="0 0 580 690" role="img" aria-label="Christmas tree formed from snowflakes, saxophone, piano keys, microphone, cocktail glass and music notes">
    <defs>
      <linearGradient id="treeTone" x1="0" y1="0" x2="1" y2="1">
        <stop offset="0" stop-color="#efe3c8" stop-opacity="0.35"/>
        <stop offset="0.55" stop-color="#5e9ea0" stop-opacity="0.35"/>
        <stop offset="1" stop-color="#c8323a" stop-opacity="0.3"/>
      </linearGradient>
    </defs>
    <polygon points="290,0 580,690 0,690" fill="url(#treeTone)"/>
  </svg>

  <h1 class="show-title" aria-label="A Plum Hush">
    <span class="title-article">a</span>
    <span class="title-word first">plum</span>
    <span class="title-word second">hush</span>
  </h1>
  <p class="show-date">December 18th, 2015</p>

  <footer class="sponsor-band">
    <svg width="800" height="180" viewBox="0 0 800 180" aria-hidden="true">
      <path d="M0 18 Q400 -10 800 18 L800 180 L0 180 Z" fill="var(--berry)"/>
      <path d="M0 26 Q400 0 800 26 L800 180 L0 180 Z" fill="var(--snow)"/>
    </svg>
    <p class="sponsor-heading">SPONSORED BY</p>
    <div class="sponsor-list">
      <span class="sponsor-name"><span class="dot"></span>StepWorks Dance</span>
      <span class="sponsor-name">Brinley</span>
      <span class="sponsor-name">Marlo Lens Photography</span>
    </div>
    <div class="ticket-line">
      <span>for tickets 512-555-0148 ext 207</span>
      <span>WWW.VEL-NOVA.ORG</span>
    </div>
  </footer>
</main>
</body>
</html>
```